Kestrel Business Accountants , logo & business card design

I am a business consultant & accountant , servicing a range of small business clients , providing business & taxation advice.
I am looking for a logo & business card design that is not traditional accounting style.
Something colorful & innovative would be good.
Target Market(s)
Small businesses in their growth stage
Industry/Entity Type
Business Consultant
Contact Information for Business Card
Kestrel Business Accountants Pty Ltd
Peter Lamb CPA
Director
Ph: 0491 8306 42
Email : kestrel@brindlemail.com.au
On reverse of card:
"Kestrel Insight for your Business"
Business Consulting
Taxation
Superannuation
Logo styles of interest
Abstract Logo
Wordmark Logo
Look and feel
Each slider illustrates characteristics of the customer's brand and the style your logo design should communicate.

```html
<!DOCTYPE html>
<html lang="en">
<head>
<meta charset="utf-8">
<title>Kestrel Business Accountants – Business Card</title>
<link rel="stylesheet" href="https://fonts.googleapis.com/css2?family=Marcellus+SC&family=Questrial&display=swap">
<style>
  :root {
    --backdrop: #e9e4dc;
    --card-top: #6c6c6e;
    --card-bottom: #565658;
    --brand-orange: #e2712f;
    --brand-orange-faint: #8e6753;
    --text-light: #dcdcdc;
    --text-soft: #c4c4c4;
  }
  * { box-sizing: border-box; margin: 0; padding: 0; }
  html, body {
    width: 1200px;
    height: 419px;
    overflow: hidden;
    background: var(--backdrop);
  }
  .card-sheet {
    position: relative;
    width: 1200px;
    height: 419px;
    display: flex;
    justify-content: space-between;
    align-items: center;
    padding: 0 40px;
  }
  .card {
    position: relative;
    width: 540px;
    height: 304px;
    background: linear-gradient(180deg, var(--card-top), var(--card-bottom));
    overflow: hidden;
  }
  .wordmark {
    position: absolute;
    font-family: "Questrial", sans-serif;
    font-weight: 400;
    line-height: 1;
    letter-spacing: 2px;
  }
  .card-front .wordmark {
    left: 28px;
    top: 70px;
    font-size: 104px;
    color: var(--brand-orange);
  }
  .card-back .wordmark {
    left: 22px;
    top: 96px;
    font-size: 96px;
    color: var(--brand-orange-faint);
  }
  .tagline {
    position: absolute;
    right: 18px;
    bottom: 16px;
    text-align: right;
    font-family: "Marcellus SC", serif;
    color: var(--text-light);
  }
  .tagline-motto {
    font-size: 19px;
    letter-spacing: 0.3px;
  }
  .tagline-services {
    font-size: 10.5px;
    letter-spacing: 0.6px;
    color: var(--text-soft);
    margin-top: 2px;
  }
  .contact {
    position: absolute;
    right: 18px;
    top: 30px;
    text-align: right;
    font-family: "Questrial", sans-serif;
    color: var(--text-light);
  }
  .contact-name { font-size: 23px; }
  .contact-role {
    font-size: 14px;
    font-style: italic;
    color: var(--text-soft);
    margin-top: 3px;
  }
  .contact-details {
    list-style: none;
    margin-top: 30px;
    font-size: 15.5px;
    line-height: 1.5;
  }
  .company-name {
    position: absolute;
    left: 0;
    right: 0;
    bottom: 16px;
    text-align: center;
    font-family: "Marcellus SC", serif;
    font-size: 21px;
    letter-spacing: 0.4px;
    color: var(--text-light);
  }
</style>
</head>
<body>
  <main class="card-sheet">
    <section class="card card-front" aria-label="Card front">
      <div class="wordmark">Kestrel</div>
      <div class="tagline">
        <p class="tagline-motto">“Kestrel Insight for your Business”</p>
        <p class="tagline-services">Business - Consulting - Taxation - Superannuation</p>
      </div>
    </section>

    <section class="card card-back" aria-label="Card back">
      <div class="wordmark" aria-hidden="true">Kestrel</div>
      <div class="contact">
        <p class="contact-name">Peter Lamb</p>
        <p class="contact-role">CPA Director</p>
        <ul class="contact-details">
          <li>P: 0491 8306 42</li>
          <li>E: kestrel@brindlemail.com.au</li>
        </ul>
      </div>
      <p class="company-name">Kestrel Business Accountants Pty Ltd</p>
    </section>
  </main>
</body>
</html>
```